Larkfield Property Maintenance needs a logo and business card

Maintenance company providing Residential/Commercial small building and maintenance works.This start up company needs a professional image with a new logo/business card.

The company name is 'Larkfield Property Maintenance'

The logo/business card should use the colour ORANGE.

Would like solid colour orange with logo on one side.
Name and business details on the other.

I would like a picture of a 'house' as part of the logo.

Need to be professional and classy but with a slightly softer edge to appeal to female as well as male clients.

The text on the card and tag line for the business to be included on the card as follows:

"Larkfield Property Maintenance
A promise of quality with outstanding service ..."

Declan Whitby

(Icons for Ph. Email. Mob. and Web address)

MOB. 0412 578 319
PH. 03 9617 2248
Email: declan@larkfieldpropertymaintenance.com.au
Address: 47 Tilbury Lane, Ashbury Heights VIC 3288
Web: larkfieldpropertymaintenance.com.au

Target Market(s)

35 to 55 year old time poor professional white collar

Industry/Entity Type

Building

Logo Text

Larkfield Property Maintenance (tag line: A Commitment to Quality and Exceptional Service)

Font styles to use
Sans Serif

Requirements
Must have
• The logo picture should be of a house
Should not have
• Do not want references to orange 'fruit' in the design

```html
<!DOCTYPE html>
<html lang="en">
<head>
<meta charset="utf-8">
<title>Larkfield Property Maintenance – Business Card and Logo</title>
<link href="https://fonts.googleapis.com/css2?family=Open+Sans:wght@400;600;700&display=swap" rel="stylesheet">
<style>
  :root {
    --orange: #f26a10;
    --panel-grey: #e3e3e3;
    --white: #ffffff;
    --ink: #333333;
    --muted: #777777;
  }
  * { box-sizing: border-box; margin: 0; padding: 0; }
  html, body { width: 1200px; height: 436px; overflow: hidden; background: var(--white); }
  body { font-family: "Open Sans", Arial, sans-serif; color: var(--ink); position: relative; }

  .stage-card { position: absolute; left: 0; top: 0; width: 694px; height: 436px; background: var(--panel-grey); }
  .stage-logo { position: absolute; left: 694px; top: 0; width: 506px; height: 436px; background: var(--white); }

  .business-card {
    position: absolute; left: 75px; top: 80px; width: 586px; height: 307px;
    background: var(--white); border-radius: 8px; overflow: hidden;
    box-shadow: 0 1px 3px rgba(0,0,0,0.08);
  }

  .brand-mark { position: absolute; background: var(--orange); border-radius: 6px; }
  .brand-name { position: absolute; color: var(--orange); font-weight: 600; text-transform: uppercase; white-space: nowrap; }
  .brand-name .name-main { display: block; line-height: 1; letter-spacing: 0.5px; }
  .brand-name .name-sub { display: block; line-height: 1.2; }

  .card-mark { left: 170px; top: 24px; width: 84px; height: 84px; }
  .card-name { left: 266px; top: 60px; }
  .card-name .name-main { font-size: 31px; }
  .card-name .name-sub { font-size: 11.5px; margin-top: 5px; }

  .showcase-mark { left: 58px; top: 150px; width: 150px; height: 150px; border-radius: 10px; }
  .showcase-name { left: 223px; top: 212px; }
  .showcase-name .name-main { font-size: 44px; }
  .showcase-name .name-sub { font-size: 18px; margin-top: 10px; }

  .holder { position: absolute; right: 386px; top: 195px; text-align: right; }
  .holder-name { color: var(--orange); font-weight: 600; font-size: 12px; letter-spacing: 0.3px; text-transform: uppercase; }
  .holder-role { color: var(--muted); font-size: 10px; margin-top: 3px; }

  .divider {
    position: absolute; left: 244px; top: 172px; width: 2px; height: 74px;
    background: linear-gradient(to bottom, rgba(150,150,150,0), #9a9a9a 50%, rgba(150,150,150,0));
  }

  .contact-list { position: absolute; left: 282px; top: 151px; list-style: none; }
  .contact-list li { display: flex; align-items: center; height: 20.5px; font-size: 10.5px; color: var(--ink); white-space: nowrap; }
  .contact-list svg { width: 11px; height: 11px; margin-right: 8px; flex: none; fill: var(--orange); }

  .tagline-band {
    position: absolute; left: 0; bottom: 0; width: 100%; height: 31px;
    background: var(--orange); color: var(--white);
    display: flex; align-items: center; justify-content: center; font-size: 11.5px;
  }
</style>
</head>
<body>
  <section class="stage-card">
    <article class="business-card">
      <span class="brand-mark card-mark"></span>
      <p class="brand-name card-name">
        <span class="name-main">Larkfield</span>
        <span class="name-sub">Property Maintenance</span>
      </p>

      <div class="holder">
        <p class="holder-name">Declan Whitby</p>
        <p class="holder-role">Company CEO</p>
      </div>

      <span class="divider"></span>

      <ul class="contact-list">
        <li>
          <svg viewBox="0 0 12 12" aria-hidden="true"><path d="M3 0h6a1 1 0 0 1 1 1v10a1 1 0 0 1-1 1H3a1 1 0 0 1-1-1V1a1 1 0 0 1 1-1zm0 1.5v8h6v-8zm3 8.7a.6.6 0 1 0 0 1.2.6.6 0 0 0 0-1.2z"/></svg>
          0412 578 319
        </li>
        <li>
          <svg viewBox="0 0 12 12" aria-hidden="true"><path d="M2.4 0.5l2 2.4-1 1.5c.8 1.6 2 2.8 3.6 3.6l1.5-1 2.4 2-1.1 1.9C5.6 10.8 1.2 6.4.5 1.6z"/></svg>
          03 9617 2248
        </li>
        <li>
          <svg viewBox="0 0 12 12" aria-hidden="true"><path d="M0.5 2h11v8h-11zm1.3 1l4.2 3.2L10.2 3zm-.3 1v5h9V4L6 7.4z"/></svg>
          declan@larkfieldpropertymaintenance.com.au
        </li>
        <li>
          <svg viewBox="0 0 12 12" aria-hidden="true"><circle cx="6" cy="6" r="5.5"/><path d="M3 4.5c1 .2 1.5 1 1.2 2 .8.4 1 1.2.6 2.3M8 2.2c-.6.8-.3 1.6.6 2 .6.3.9 1 .6 1.6" stroke="#fff" stroke-width="1" fill="none"/></svg>
          larkfieldpropertymaintenance.com.au
        </li>
        <li>
          <svg viewBox="0 0 12 12" aria-hidden="true"><path d="M6 0.3a4 4 0 0 1 4 4c0 3-4 7.4-4 7.4S2 7.3 2 4.3a4 4 0 0 1 4-4zm0 2.4a1.6 1.6 0 1 0 0 3.2 1.6 1.6 0 0 0 0-3.2z"/></svg>
          47 Tilbury Lane, Ashbury Heights VIC 3288
        </li>
      </ul>

      <div class="tagline-band">A promise of quality with outstanding service</div>
    </article>
  </section>

  <section class="stage-logo">
    <span class="brand-mark showcase-mark"></span>
    <p class="brand-name showcase-name">
      <span class="name-main">Larkfield</span>
      <span class="name-sub">Property Maintenance</span>
    </p>
  </section>
</body>
</html>
```